Business Card Design

Provide project management services to the construction and other industries
Construction services - Civil and Concrete works
Shop Detailing
Structural Modelling
Client side coordination of project teams and consultants
Feasibility Studies for construction projects

Industry/Entity Type

Business

Contact Information for Business Card

Plan Sure
Derek Calloway B.Eng (Hons), G.C.Bus.
Director

m: 0412 738 564
e: dcalloway@plansure.com.au

p: 08 6358 2714
a: 17 Banksia Court, Stirling, WA 6021

```html
<!DOCTYPE html>
<html lang="en">
<head>
<meta charset="utf-8">
<title>Plan Sure – Business Card</title>
<link rel="stylesheet" href="https://fonts.googleapis.com/css2?family=Arimo:wght@400;700&family=Open+Sans:wght@400;700&display=swap">
<style>
  :root {
    --backdrop: #5b3e2c;
    --card-black: #141414;
    --brand-green: #0b9a12;
    --ink: #111111;
    --ink-soft: #2b2b2b;
    --paper: #ffffff;
  }
  * { box-sizing: border-box; margin: 0; padding: 0; }
  html, body { width: 1200px; height: 1000px; overflow: hidden; }
  body { background: var(--backdrop); position: relative; }

  .card {
    position: absolute;
    left: 293px;
    width: 612px;
    height: 360px;
    box-shadow: 0 4px 10px rgba(0,0,0,0.45);
    overflow: hidden;
  }

  /* Front */
  .card--front { top: 125px; background: var(--card-black); }
  .card--front .brand-name {
    position: absolute; top: 86px; left: 0; width: 100%;
    text-align: center;
    font-family: "Arimo", Arial, sans-serif; font-weight: 700;
    font-size: 50px; letter-spacing: 0.5px;
    color: var(--paper);
  }
  .service-band {
    position: absolute; left: 0; top: 227px; width: 100%; height: 133px;
    background: var(--brand-green);
    padding: 34px 25px 0 25px;
  }
  .service-line {
    font-family: "Arimo", Arial, sans-serif; font-size: 18px;
    line-height: 23px; color: var(--ink);
    text-align: justify; text-align-last: justify;
    white-space: nowrap;
  }
  .service-line .sep { margin: 0 4px; }

  /* Back */
  .card--back { top: 515px; height: 357px; background: var(--paper); }
  .card--back .brand-name {
    position: absolute; top: 88px; left: 0; width: 100%;
    text-align: center;
    font-family: "Arimo", Arial, sans-serif; font-weight: 700;
    font-size: 50px; letter-spacing: 0.5px;
    color: var(--ink);
  }
  .person {
    position: absolute; top: 195px; left: 0; width: 100%;
    text-align: center;
    font-family: "Open Sans", Calibri, sans-serif; color: var(--ink-soft);
  }
  .person__name { font-weight: 700; font-size: 18px; line-height: 24px; color: var(--ink); }
  .person__detail { font-size: 15.5px; line-height: 23px; }
  .contact {
    position: absolute; top: 297px; left: 0; width: 100%;
    text-align: center;
    font-family: "Open Sans", Calibri, sans-serif; color: var(--ink-soft);
    font-size: 14.5px; line-height: 26px;
  }
  .contact .sep { margin: 0 6px; color: #555; }
  .contact .sep--accent { color: var(--brand-green); }
</style>
</head>
<body>
  <section class="card card--front" aria-label="Business card front">
    <div class="brand-name">PLAN SURE</div>
    <div class="service-band">
      <p class="service-line">Project Management Services <span class="sep">|</span> Civil and Concrete Works</p>
      <p class="service-line">Construction Services <span class="sep">|</span> Shop Detailing <span class="sep">|</span> Client Side Coordination</p>
      <p class="service-line">Structural Modelling <span class="sep">|</span> Feasibility Studies For Construction Projects</p>
    </div>
  </section>

  <section class="card card--back" aria-label="Business card back">
    <div class="brand-name">PLAN SURE</div>
    <div class="person">
      <p class="person__name">Derek Calloway</p>
      <p class="person__detail">B.Eng (Hons), G.C.Bus.</p>
      <p class="person__detail">Director</p>
    </div>
    <div class="contact">
      <p>17 Banksia Court, Stirling, WA 6021</p>
      <p>M: 0412 738 564<span class="sep">|</span>P: 08 6358 2714<span class="sep sep--accent">|</span>E: dcalloway@plansure.com.au</p>
    </div>
  </section>
</body>
</html>
```